Revamp our wedding venue website

Currently we are using wordpress for our website and hoped to find a designer that can assist us with making the website prettier and more pleasing and draw more interest. www.velmorhall.net is our current site. We are connected to google business mail, so I would prefer to stay with this for now and update our gallery with new photos, blog page and putting the contact us form back on all the pages.

Target Market(s)

20-40 years of age, all ranges of styles and generally clients looking for a different modern feel vs. a hotel hall.

Industry/Entity Type

Wedding

Logo Text

1947 Velmor Hall

Number of Pages Required

4 page

Font styles to use
Serif

Requirements
Must have
• Light, airy feel. Romantic and informative. Mobile friendly and easy to contact us-preferred contact form on all pages. Gallery of photos. Previous reviews
Nice to have
• Bio of staff, maybe some videos, and fun things to do in the area for out of town guests. Maps and also venue blank floor plan.

```html
<!DOCTYPE html>
<html lang="en">
<head>
<meta charset="utf-8">
<title>1947 Velmor Hall – Weddings &amp; Events</title>
<link href="https://fonts.googleapis.com/css2?family=Cinzel:wght@400;700&family=Great+Vibes&family=Raleway:wght@400;500;600&family=Open+Sans:wght@400;600&display=swap" rel="stylesheet">
<style>
:root{
  --magenta:#c2127f;
  --red:#d9232d;
  --ink:#222;
  --text:#444;
  --navy:#1e2f78;
  --rule:#cfcfcf;
  --white:#fff;
  --blush:#f2c6d4;
  --petal:#e88fb0;
  --cream:#f6f1ec;
  --sand:#d8c3ad;
}
*{box-sizing:border-box;margin:0;padding:0}
html,body{width:1200px;height:3600px;overflow:hidden;background:var(--white)}
body{position:relative;font-family:"Open Sans",sans-serif;color:var(--text)}

/* header */
.site-header{position:absolute;left:0;top:0;width:1200px;height:79px;background:var(--white)}
.brand{position:absolute;left:53px;top:18px;font-family:"Cinzel",serif;font-size:26px;color:var(--ink);letter-spacing:.5px}
.main-nav{position:absolute;top:30px;left:0;width:1200px;font-family:"Raleway",sans-serif;font-size:16px;color:var(--ink)}
.main-nav span{position:absolute;white-space:nowrap}
.main-nav .active::after{content:"";position:absolute;left:-8px;right:-8px;top:46px;height:4px;background:var(--magenta)}

/* hero */
.hero{position:absolute;left:0;top:79px;width:1200px;height:576px;
  background:
    radial-gradient(circle at 62% 18%,rgba(236,140,176,.55) 0,rgba(236,140,176,0) 9%),
    radial-gradient(circle at 80% 30%,rgba(242,170,196,.6) 0,rgba(242,170,196,0) 8%),
    radial-gradient(circle at 72% 62%,rgba(229,120,160,.45) 0,rgba(229,120,160,0) 10%),
    radial-gradient(circle at 92% 75%,rgba(240,180,200,.55) 0,rgba(240,180,200,0) 9%),
    radial-gradient(ellipse at 70% 55%,rgba(120,128,148,.55) 0,rgba(120,128,148,0) 30%),
    radial-gradient(ellipse at 88% 45%,rgba(255,255,255,.9) 0,rgba(255,255,255,0) 28%),
    linear-gradient(90deg,#f7f3ee 0%,#efe7df 35%,#d9cdc2 58%,#ede4dc 78%,#f4ece6 100%)}
.hero-title{position:absolute;left:65px;top:219px;font-family:"Cinzel",serif;font-size:46px;line-height:54px;color:var(--ink)}
.hero-title .accent{color:var(--magenta);display:block}
.hero-sub{position:absolute;left:65px;top:334px;width:470px;font-family:"Raleway",sans-serif;font-size:22px;line-height:27px;color:var(--ink)}
.btn{position:absolute;display:flex;align-items:center;justify-content:center;font-family:"Open Sans",sans-serif;font-weight:600;font-size:17px}
.btn-primary{left:65px;top:420px;width:189px;height:48px;background:var(--magenta);color:var(--white)}
.btn-outline{left:283px;top:420px;width:192px;height:48px;background:var(--white);border:2px solid var(--magenta);color:var(--ink)}

/* section headings */
.script-heading{position:absolute;left:0;width:1200px;text-align:center;font-family:"Great Vibes",cursive;font-size:66px;color:var(--ink);font-weight:700}
.divider{position:absolute;left:192px;width:816px;height:20px}

/* testimonials */
.review{position:absolute;width:216px;text-align:center}
.review-photo{position:absolute;left:26px;top:0;width:164px;height:164px;border-radius:50%;border:4px solid var(--navy)}
.review-title{position:absolute;left:0;width:100%;font-family:"Raleway",sans-serif;font-size:22px;line-height:24px;color:var(--ink)}
.review-quote{position:absolute;left:8px;width:200px;font-size:13.5px;line-height:20px;color:var(--text)}
.review-name{position:absolute;left:0;width:100%;font-family:"Raleway",sans-serif;font-size:17px;color:var(--magenta)}
.review-card{position:absolute;left:487px;top:847px;width:247px;height:490px;border:1px solid #d6d6d6}
.btn-more{left:451px;top:1373px;width:293px;height:43px;background:var(--red);color:var(--white);font-size:17px;font-weight:400;border-radius:3px}

/* feature band */
.band{position:absolute;left:0;top:1490px;width:1200px;height:538px;
  background:
    radial-gradient(ellipse at 30% 55%,rgba(255,255,255,.75) 0,rgba(255,255,255,0) 18%),
    radial-gradient(ellipse at 32% 42%,rgba(70,72,92,.45) 0,rgba(70,72,92,0) 14%),
    linear-gradient(180deg,rgba(180,200,210,.55) 0%,rgba(180,200,210,0) 28%,rgba(0,0,0,0) 72%,rgba(110,70,60,.35) 100%),
    linear-gradient(90deg,#d9c6b0 0%,#c9ab94 28%,#d58fae 50%,#d676a4 75%,#cf6b9c 100%)}
.band-title{position:absolute;left:540px;top:1602px;width:600px;text-align:center;font-family:"Great Vibes",cursive;font-size:44px;line-height:48px;color:var(--white)}
.band-text{position:absolute;left:560px;top:1712px;width:560px;text-align:center;font-size:19px;line-height:33px;color:var(--white)}

/* gallery */
.filter{position:absolute;top:2232px;height:43px;display:flex;align-items:center;justify-content:center;border:2px solid var(--magenta);font-size:14px;color:var(--ink)}
.filter.active{background:var(--magenta);color:var(--white)}
.tile{position:absolute;width:341px;height:230px}
.tile::after{content:"";position:absolute;inset:14px;border:1px solid rgba(255,255,255,.85)}
.tile-caption{position:absolute;left:72px;top:2345px;width:310px;height:195px;background:rgba(20,20,20,.82);z-index:2;text-align:center;color:var(--white)}
.tile-caption h3{font-family:"Cinzel",serif;font-size:23px;font-weight:400;margin-top:48px;letter-spacing:1px}
.tile-caption p{font-size:14px;font-weight:600;line-height:22px;margin:12px 28px 0}

/* contact */
.contact{position:absolute;left:0;top:2897px;width:1200px;height:650px;background:
  radial-gradient(ellipse at 20% 30%,rgba(90,90,90,.6) 0,rgba(90,90,90,0) 30%),
  radial-gradient(ellipse at 80% 60%,rgba(85,85,85,.6) 0,rgba(85,85,85,0) 30%),
  linear-gradient(180deg,#454545,#3a3a3a)}
.contact-heading{position:absolute;left:0;top:2930px;width:1200px;text-align:center;font-family:"Raleway",sans-serif;font-weight:500;font-size:40px;color:var(--white)}
.contact-info{position:absolute;left:0;width:1200px;text-align:center;font-size:15px;color:#e8e8e8}
.contact-info.strong{font-weight:600;color:var(--white)}
.field{position:absolute;background:var(--white);border-radius:3px;font-size:14px;color:#888;padding:13px 16px}
.btn-submit{left:535px;top:3458px;width:132px;height:39px;background:#9a9a9a;color:var(--white);font-weight:400;font-size:15px;border-radius:3px}

.site-footer{position:absolute;left:0;top:3547px;width:1200px;height:53px;background:var(--magenta);display:flex;align-items:center;justify-content:center;font-size:14px;color:var(--white)}
</style>
</head>
<body>

<header class="site-header">
  <div class="brand">1947 Velmor Hall</div>
  <nav class="main-nav">
    <span class="active" style="left:497px">HOME</span>
    <span style="left:589px">WEDDINGS</span>
    <span style="left:716px">EVENTS</span>
    <span style="left:823px">CATERING</span>
    <span style="left:945px">GALLERY</span>
    <span style="left:1059px">CONTACT US</span>
  </nav>
</header>

<section class="hero" role="img" aria-label="Photo of a bride and groom about to kiss under falling rose petals beside a white balustrade"></section>
<h1 class="hero-title">A Wonderful Day of<span class="accent">Love And Fun.</span></h1>
<p class="hero-sub">Tampa's Most Unique Wedding and Events Venue 813.555.0147</p>
<div class="btn btn-primary">Find A Couple</div>
<div class="btn btn-outline">Sign Up</div>

<h2 class="script-heading" style="top:672px">What you say:</h2>
<svg class="divider" style="top:766px" viewBox="0 0 816 20"><line x1="0" y1="10" x2="816" y2="10" stroke="#cfcfcf" stroke-width="2"/></svg>

<div class="review-card"></div>

<div class="review" style="left:19px;top:873px">
  <div class="review-photo" style="background:radial-gradient(circle at 50% 42%,#f0d2bf 0,#d3a58a 30%,#6f8a4e 62%,#3f5a2e 100%)" role="img" aria-label="Portrait of a laughing bride outdoors"></div>
  <div class="review-title" style="top:184px">Excellent<br>Craftsmanship</div>
  <p class="review-quote" style="top:246px">"I received my wedding album today and I just don't know what to say. It is the most lovely album I have ever seen. The craftsmanship is excellent!"</p>
  <div class="review-name" style="top:393px">Jordan P.</div>
</div>

<div class="review" style="left:247px;top:873px">
  <div class="review-photo" style="background:radial-gradient(circle at 50% 45%,#ecc9b2 0,#c79478 32%,#4c3a33 62%,#d9d2c8 100%)" role="img" aria-label="Portrait of a smiling couple"></div>
  <div class="review-title" style="top:184px">Excellent<br>Craftsmanship</div>
  <p class="review-quote" style="top:246px">"We are so happy with our album! Golden Keepsake Album's service was amazing -very easy to work with in all of the design stages. VERY IMPRESSED!"</p>
  <div class="review-name" style="top:393px">Nadia &amp; Oscar S.</div>
</div>

<div class="review" style="left:502px;top:873px">
  <div class="review-photo" style="background:radial-gradient(circle at 50% 45%,#efcfb8 0,#c9977a 30%,#2f3a4e 60%,#8fae70 100%)" role="img" aria-label="Portrait of a couple outdoors"></div>
  <div class="review-title" style="top:184px">Classy &amp;<br>Professional</div>
  <p class="review-quote" style="top:246px">"The layouts are classy and professional. It's exciting to send your photos off and see what they come up with and then to still be able to make as many changes as you like."</p>
  <div class="review-name" style="top:407px">-Elena &amp; Marcus G</div>
</div>

<div class="review" style="left:727px;top:873px">
  <div class="review-photo" style="background:radial-gradient(circle at 50% 45%,#f3d8c4 0,#e0b58c 34%,#c99a5c 58%,#eef0e8 100%)" role="img" aria-label="Portrait of a smiling blonde bride"></div>
  <div class="review-title" style="top:184px">Brilliant<br>customer service</div>
  <p class="review-quote" style="top:246px">"The photos look clear and crisp. Excellent pricing and brilliant customer service - always willing to accommodate all of my suggestions."</p>
  <div class="review-name" style="top:372px">Rosa M.</div>
</div>

<div class="review" style="left:967px;top:873px">
  <div class="review-photo" style="background:radial-gradient(circle at 50% 45%,#f0cfb6 0,#cf9c7d 32%,#2a2426 60%,#e8dcd2 100%)" role="img" aria-label="Portrait of a couple cheek to cheek"></div>
  <div class="review-title" style="top:184px">Completely<br>satisfied</div>
  <p class="review-quote" style="top:246px">"Golden Keepsake Albums worked so hard and diligently with us to make sure we were completely satisfied - Everyone who has seen our album is amazed!"</p>
  <div class="review-name" style="top:390px">Jordan P.</div>
</div>

<div class="btn btn-more">See more customer reviews
  <svg width="14" height="10" viewBox="0 0 14 10" style="margin-left:8px"><path d="M2 2 L7 7 L12 2" fill="none" stroke="#fff" stroke-width="2"/></svg>
</div>

<section class="band" role="img" aria-label="Photo of a bride and groom sitting together on a wooden pier by the water"></section>
<h2 class="band-title">Weddings &amp; Events at the<br>1947 Velmor Hall</h2>
<p class="band-text">Weddings &amp; Events at the 1947 Velmor Hall<br>imagine your wedding or event in Tampa's premiere, unique<br>and historic venue</p>

<h2 class="script-heading" style="top:2072px">Our Gallery</h2>
<svg class="divider" style="top:2165px" viewBox="0 0 816 20"><line x1="0" y1="10" x2="816" y2="10" stroke="#cfcfcf" stroke-width="2"/></svg>

<div class="filter active" style="left:334px;width:57px">All</div>
<div class="filter" style="left:413px;width:120px">Engagement</div>
<div class="filter" style="left:554px;width:96px">Wedding</div>
<div class="filter" style="left:672px;width:72px">Party</div>
<div class="filter" style="left:766px;width:93px">DJ Night</div>

<div class="tile" style="left:58px;top:2328px;background:radial-gradient(ellipse at 60% 40%,#a07a62 0,#5d4034 45%,#2b2220 100%)" role="img" aria-label="Photo of wedding table decoration"></div>
<div class="tile-caption"><h3>DECORATION</h3><p>Lorem ipsum dolor sit amet, consectetur adipisicing elit. Repudiandae quia eligendi libero</p></div>
<div class="tile" style="left:420px;top:2328px;background:linear-gradient(180deg,#7fbde0 0%,#a9d3e6 30%,#cfe2e6 42%,#e9e1d2 55%,#c9a8d4 72%,#f0e6ea 100%)" role="img" aria-label="Photo of a beach wedding aisle with purple-draped chairs and a canopy"></div>
<div class="tile" style="left:780px;top:2328px;background:radial-gradient(ellipse at 60% 40%,#ffffff 0,#f1e6e6 30%,#e7b7c6 48%,#c4b0a2 75%,#8f7a6c 100%)" role="img" aria-label="Photo of a tiered wedding cake with pink roses"></div>
<div class="tile" style="left:58px;top:2580px;background:radial-gradient(ellipse at 55% 50%,#f7f6ef 0,#dfe3cf 32%,#b9c2a2 52%,#eeeae3 80%,#d9d3ca 100%)" role="img" aria-label="Photo of a bride holding a white rose bouquet"></div>
<div class="tile" style="left:420px;top:2580px;background:radial-gradient(ellipse at 58% 45%,#ffffff 0,#f0dfe3 28%,#d98aa6 45%,#6e5450 70%,#2f2424 100%)" role="img" aria-label="Photo of a wedding cake decorated with pink roses"></div>
<div class="tile" style="left:780px;top:2580px;background:radial-gradient(ellipse at 60% 45%,#fbf6ef 0,#ead6bd 30%,#c99a6e 58%,#9a6a46 85%,#e8d9c8 100%)" role="img" aria-label="Photo of a server setting a banquet table"></div>

<section class="contact" role="img" aria-label="Darkened background photo behind the contact section"></section>
<h2 class="contact-heading">Contact Us</h2>
<svg class="divider" style="top:2990px" viewBox="0 0 816 20"><line x1="0" y1="10" x2="816" y2="10" stroke="#bdbdbd" stroke-width="2"/></svg>
<div class="contact-info strong" style="top:3032px">1947 VELMOR HALL</div>
<div class="contact-info" style="top:3073px">We're conveniently located in historic Ybor City at:</div>
<div class="contact-info" style="top:3102px">1947 East 9th Ave.</div>
<div class="contact-info" style="top:3131px">Tampa, FL 33605</div>
<div class="contact-info" style="top:3157px">Email : Events@VelmorHall.net</div>

<div class="field" style="left:302px;top:3211px;width:291px;height:46px">First Name*</div>
<div class="field" style="left:605px;top:3211px;width:290px;height:46px">Last Name*</div>
<div class="field" style="left:302px;top:3266px;width:291px;height:48px">Email*</div>
<div class="field" style="left:605px;top:3266px;width:290px;height:48px">Phone No</div>
<div class="field" style="left:302px;top:3324px;width:593px;height:110px">Message</div>
<div class="btn btn-submit">SUBMIT</div>

<footer class="site-footer">© Copyright 2016 1947 Velmor Hall. All Right Reservrd</footer>

</body>
</html>
```